UI Kit for Contractor Websites

I created a wireframe in Webflow and want to create a number of templates around that. There are existing templates, but I a few built around my content structure.

The types of clients are home remodeling services (homebuilders, plumbers, painters, electricians, handymen, etc.)

https://site-draft-7bc41d92e30-fd19a2b84c07e.pagehost.example/

*Use the website copy content from here but you do NOT need to follow the wireframe so plug it in however you feel best. Eventually, we'll have multiple types of heroes, services, etc.

I'd like to start with the first homepage template. The homepage templates will all have the same fonts, color scheme, and content. Once we finish about 5 of those, we'd move onto the next stage.

https://www.clipvault.example/share/5d8e0b31f7a249c6b0e2a9f41c7d3e88

Other clean, modern, UI kits (templates) or websites I like:
https://www.brimlow.example/
https://vector-layout.pagehost.example/
https://quillet.example/
https://tern-layout.pagehost.example/
https://www.plotnest.example/talebrick-website-templates
https://relay-layout.pagehost.example/
https://tiles-layout.pagehost.example/

*We'd likely have a lot of images, not illustrations since the client type we're building is pretty visual. Can use dummy photos.

Home

Navbar

Hero Section
Preheader (H1)
Hero Header (H2)
Hero CTA
Hero Secondary CTA

Hero Testimonial Short Quote
Hero Testimonial Name

Social Proof (CMS, can be multiple or one)
Testimonial Quote
Testimonial Name
Testimonial Image

CTA
CTA Headline
CTA Subheadline
CTA Button

Features/Value Stack
Value Stack H2
Value 1 Headline (H3)
Value 1 Description
Value 2 Headline (H3)
Value 2 Description
Value 3 Headline (H3)
Value 3 Description

Services (CMS, can be multiple)
Service Name
Service Short Description
CTA: Get Quote
Main Image

Homepage How It Works
Homepage How It Works Headline
How it Works Subheadline
Step 1 Name
Step 1 Description
Step 2 Name
Step 2 Description
Step 3 Name
Step 3 Description

About/Founder’s Note/Team
Homepage Founder Note Headline
Founder Note or About Info
Owner Signature
CTA to About Page

CTA
CTA Headline
CTA Subheadline
CTA Button

Footer

```html
<!DOCTYPE html>
<html lang="en">
<head>
<meta charset="utf-8">
<title>Home Remodeling Services – Homepage</title>
<link rel="stylesheet" href="https://fonts.googleapis.com/css2?family=Inter:wght@400;500;600;700;800&display=swap">
<style>
:root{
  --accent:#F5B12B;
  --accent-deep:#EE8A17;
  --accent-soft:#FFF3CF;
  --ink:#111827;
  --ink-soft:#4B5563;
  --muted:#8A8F99;
  --panel:#F2F2F3;
  --white:#FFFFFF;
  --footer:#1F2330;
  --footer-text:#B8BCC6;
}
*{box-sizing:border-box;margin:0;padding:0}
html,body{width:1200px;height:4744px;overflow:hidden}
body{font-family:"Inter",Arial,sans-serif;color:var(--ink);background:var(--white);position:relative}
.abs{position:absolute}
.btn{display:inline-flex;align-items:center;justify-content:center;height:36px;padding:0 20px;border-radius:4px;font-size:12px;font-weight:700;letter-spacing:.04em;text-transform:uppercase;white-space:nowrap}
.btn-accent{background:var(--accent);color:var(--white)}
.btn-outline{border:2px solid var(--ink);color:var(--ink);background:var(--white)}
.btn-dark{background:var(--ink);color:var(--white)}
.section-title{position:absolute;left:0;width:1200px;text-align:center;font-size:44px;font-weight:700;letter-spacing:-.01em}
.photo{position:absolute;border-radius:6px}

/* nav */
.logo{left:88px;top:30px;font-size:26px;font-weight:800;letter-spacing:-.02em}
.nav{right:88px;top:24px;display:flex;align-items:center;gap:28px;font-size:12px;font-weight:600;text-transform:uppercase}
.nav .btn{height:38px}

/* hero */
.hero-frame{left:584px;top:136px;width:300px;height:568px;border:4px solid var(--accent);border-radius:4px}
.hero-photo{left:608px;top:88px;width:504px;height:600px;background:linear-gradient(160deg,#dfe3e8 0%,#9eb0c4 45%,#3f5f86 100%)}
.preheader{font-size:12px;font-weight:700;color:var(--accent);text-transform:uppercase;letter-spacing:.06em}
.hero-pre{left:88px;top:250px}
.hero-title{left:88px;top:272px;width:480px;font-size:44px;line-height:1.08;font-weight:800;letter-spacing:-.02em}
.hero-ctas{left:88px;top:448px;display:flex;gap:14px}
.stars{left:88px;top:504px;display:flex;gap:4px}
.hero-quote{left:88px;top:528px;font-size:15px;font-weight:500}
.hero-name{left:88px;top:552px;font-size:13px;color:var(--muted)}

/* features */
.feature{position:absolute;top:880px;width:300px;text-align:center}
.feature svg{display:block;margin:0 auto 24px}
.feature h3{font-size:22px;font-weight:700;margin-bottom:10px}
.feature p{font-size:14px;line-height:1.5;color:var(--ink-soft);width:270px;margin:0 auto}

/* how it works */
.how-panel{left:88px;top:1216px;width:1024px;height:568px;background:var(--panel);border-radius:14px;overflow:hidden}
.how-photo{position:absolute;right:40px;bottom:0;width:430px;height:560px;border-radius:0;background:radial-gradient(ellipse at 50% 55%,#f4dfa8 0%,#e9c56b 30%,#ef7f25 55%,var(--panel) 75%)}
.how-title{position:absolute;left:96px;top:124px;font-size:44px;font-weight:700}
.step{position:absolute;left:96px;display:flex;gap:22px}
.step-num{width:48px;height:48px;background:var(--accent);color:var(--white);font-size:26px;font-weight:700;display:flex;align-items:center;justify-content:center;border-radius:3px;flex:none}
.step h3{font-size:18px;font-weight:700;margin-bottom:6px}
.step p{font-size:13px;line-height:1.45;color:var(--ink-soft);width:310px}

/* services */
.service-card{position:absolute;top:1960px;width:324px;height:472px;background:var(--white);border-radius:10px;box-shadow:0 6px 28px rgba(17,24,39,.10);overflow:hidden}
.service-card .photo{left:0;top:0;width:100%;height:240px;border-radius:10px 10px 0 0}
.service-card h3{position:absolute;left:24px;top:272px;font-size:21px;font-weight:700}
.service-card p{position:absolute;left:24px;top:306px;width:276px;font-size:14px;line-height:1.5;color:var(--ink-soft)}
.service-card .btn{position:absolute;left:24px;top:392px}

/* cta band */
.cta-band{left:88px;top:2544px;width:1024px;height:408px;border-radius:14px;background:radial-gradient(circle at 85% 20%,#FFE6A3 0%,var(--accent-soft) 40%,#FFF6DB 100%);text-align:center}
.cta-band h2{position:absolute;left:0;width:100%;top:108px;font-size:44px;line-height:1.15;font-weight:700}
.cta-band p{position:absolute;left:272px;width:480px;top:218px;font-size:12px;line-height:1.5;color:var(--ink-soft)}
.cta-band .btn{position:absolute;left:444px;top:272px;height:40px;width:136px}

/* about */
.about-photo{left:88px;top:3048px;width:472px;height:400px;background:linear-gradient(150deg,#3a2a1e 0%,#a3683a 40%,#d9a15c 65%,#6a7e96 100%)}
.about-pre{left:632px;top:3096px}
.about-title{left:632px;top:3116px;font-size:46px;font-weight:700;letter-spacing:-.01em}
.about-text{left:632px;top:3180px;width:480px;font-size:14px;line-height:1.6;color:var(--ink-soft)}
.signature{left:632px;top:3316px;width:150px;height:34px;border-radius:4px;background:linear-gradient(90deg,#e9e9ec,#f5f5f6)}
.about-btn{left:632px;top:3376px}

/* testimonials */
.tcard{position:absolute;top:3656px;width:416px;height:224px;background:var(--white);border-radius:10px;box-shadow:0 6px 28px rgba(17,24,39,.10)}
.tcard .avatar{position:absolute;left:32px;top:32px;width:64px;height:64px;border-radius:50%;background:linear-gradient(135deg,#c9ced6,#7b8594)}
.tcard .name{position:absolute;left:112px;top:44px;font-size:16px;font-weight:700}
.tcard .role{position:absolute;left:112px;top:68px;font-size:12px;color:var(--muted)}
.tcard .mark{position:absolute;right:30px;top:26px}
.tcard p{position:absolute;left:32px;top:124px;width:352px;font-size:14px;line-height:1.6;color:var(--ink-soft)}

/* final cta + footer */
.footer-bg{left:0;top:4160px;width:1200px;height:584px;background:var(--footer)}
.final-cta{left:88px;top:4016px;width:1024px;height:296px;border-radius:14px;background:linear-gradient(120deg,#F4A42A 0%,var(--accent-deep) 45%,#F6B43A 100%);text-align:center;color:var(--white)}
.final-cta h2{position:absolute;left:0;width:100%;top:80px;font-size:44px;font-weight:700}
.final-cta p{position:absolute;left:272px;width:480px;top:142px;font-size:12px;line-height:1.5}
.final-cta .btn{position:absolute;left:444px;top:192px;height:40px;width:136px}
.fcol{position:absolute;top:4420px;color:var(--footer-text);font-size:13px}
.fcol h4{color:var(--white);font-size:17px;font-weight:700;margin-bottom:18px}
.fcol li{list-style:none;line-height:2}
.news-input{display:flex;margin-top:16px;width:240px;height:40px}
.news-input span{flex:1;background:var(--white);border-radius:4px 0 0 4px;color:var(--muted);font-size:12px;display:flex;align-items:center;padding-left:12px}
.news-input b{width:40px;background:var(--accent);border-radius:0 4px 4px 0;display:flex;align-items:center;justify-content:center}
.contact-row{display:flex;gap:12px;margin-bottom:14px}
.contact-row svg{flex:none;margin-top:3px}
.contact-row strong{display:block;color:var(--white);font-weight:600}
.footer-rule{left:120px;top:4650px;width:960px;height:1px;background:#343948}
.copyright{left:120px;top:4672px;color:var(--footer-text);font-size:12px}
.socials{right:120px;top:4668px;display:flex;gap:14px}
.socials i{width:20px;height:20px;border-radius:50%;background:#4A5061;display:block}
.to-top{left:1132px;top:4696px;width:36px;height:36px;border-radius:50%;background:var(--accent);display:flex;align-items:center;justify-content:center}
</style>
</head>
<body>

<div class="abs logo">LogoHere</div>
<nav class="abs nav">
  <span>Services ▾</span><span>About</span>
  <span class="btn btn-accent">Contact Us</span>
</nav>

<div class="abs hero-frame"></div>
<div class="photo hero-photo" role="img" aria-label="Plumber in a checked shirt fitting a water filter under a sink"></div>
<div class="abs preheader hero-pre">Home remodeling in seattle</div>
<h1 class="abs hero-title">Whether it's your home that needs remodeling</h1>
<div class="abs hero-ctas"><span class="btn btn-accent">Learn More</span><span class="btn btn-outline">View Projects</span></div>
<div class="abs stars">
  <svg width="90" height="16" viewBox="0 0 90 16"><g fill="#F5B12B"><path id="st" d="M8 0l2.4 5 5.6.6-4.2 3.8 1.2 5.6L8 12.2 3 15l1.2-5.6L0 5.6 5.6 5z"/><use href="#st" x="18"/><use href="#st" x="36"/><use href="#st" x="54"/><use href="#st" x="72"/></g></svg>
</div>
<p class="abs hero-quote">"These guys rock. 10 out of 10 would recommend!"</p>
<p class="abs hero-name">Dana Whitlock, Northline Inc.</p>

<h2 class="section-title" style="top:800px">Our Features</h2>
<div class="feature" style="left:90px">
  <svg width="72" height="72" viewBox="0 0 72 72" fill="none" stroke="#111827" stroke-width="3"><rect x="10" y="8" width="40" height="52" rx="3"/><circle cx="40" cy="38" r="13" stroke="#F5B12B"/><path d="M49 47l14 14" stroke-linecap="round"/></svg>
  <h3>Transparent</h3>
  <p>Eaque laudantium et beatae nobis accusamus in harum repellat quae aperiam provident.</p>
</div>
<div class="feature" style="left:450px">
  <svg width="72" height="72" viewBox="0 0 72 72" fill="none" stroke="#111827" stroke-width="3"><path d="M8 44l14-10 12 4 16-6 14 10-16 14H24z"/><rect x="26" y="10" width="20" height="14" rx="2" stroke="#F5B12B"/></svg>
  <h3>Loyalty</h3>
  <p>Eaque laudantium et beatae nobis accusamus in harum repellat quae aperiam provident.</p>
</div>
<div class="feature" style="left:810px">
  <svg width="72" height="72" viewBox="0 0 72 72" fill="none" stroke="#111827" stroke-width="3"><path d="M14 34h10v26H14zM24 36l10-20c4 0 6 3 5 7l-2 9h16c4 0 6 3 5 7l-4 16c-1 3-3 5-6 5H24"/><path d="M44 10l4 8 8 1-6 6 2 8-8-4" stroke="#F5B12B"/></svg>
  <h3>Reliable</h3>
  <p>Eaque laudantium et beatae nobis accusamus in harum repellat quae aperiam provident.</p>
</div>

<div class="abs how-panel">
  <div class="photo how-photo" role="img" aria-label="Smiling worker in hard hat and safety vest holding a drill and giving a thumbs up"></div>
  <h2 class="how-title">How It Works</h2>
  <div class="step" style="top:196px"><span class="step-num">1</span><div><h3>Get a quote</h3><p>Eaque laudantium et beatae nobis accusamus in harum. Impedit eos eaque aperiam</p></div></div>
  <div class="step" style="top:300px"><span class="step-num">2</span><div><h3>We do the job</h3><p>Eaque laudantium et beatae nobis accusamus in harum. Impedit eos eaque aperiam</p></div></div>
  <div class="step" style="top:404px"><span class="step-num">3</span><div><h3>Show off your house</h3><p>Eaque laudantium et beatae nobis accusamus in harum. Impedit eos eaque aperiam</p></div></div>
</div>

<h2 class="section-title" style="top:1886px">Our Services</h2>
<div class="service-card" style="left:88px">
  <div class="photo" role="img" aria-label="Plumber in blue overalls working on pipes" style="background:linear-gradient(135deg,#d8d2c8,#7a8aa0 55%,#2f4a78)"></div>
  <h3>Plumbers</h3><p>Eaque laudantium et beatae nobis accusamus in harum. Impedit eos eaque aperiam provident.</p>
  <span class="btn btn-accent">Get Quote</span>
</div>
<div class="service-card" style="left:438px">
  <div class="photo" role="img" aria-label="Painter rolling paint onto a wall" style="background:linear-gradient(135deg,#f1ede6,#f3b48a 50%,#8aa3c9)"></div>
  <h3>Painters</h3><p>Eaque laudantium et beatae nobis accusamus in harum. Impedit eos eaque aperiam provident.</p>
  <span class="btn btn-accent">Get Quote</span>
</div>
<div class="service-card" style="left:788px">
  <div class="photo" role="img" aria-label="Electrician in hard hat working at an electrical panel" style="background:linear-gradient(135deg,#8c5a44,#c7c9cc 50%,#3d4e6b)"></div>
  <h3>Electricians</h3><p>Eaque laudantium et beatae nobis accusamus in harum. Impedit eos eaque aperiam provident.</p>
  <span class="btn btn-accent">Get Quote</span>
</div>

<div class="abs cta-band">
  <h2>One call can solve all your<br>house problems</h2>
  <p>Sometimes you need to call in the skill and trust qualified person for the perfect repair. This is where a handyman comes in handy.</p>
  <span class="btn btn-dark">Contact Us</span>
</div>

<div class="photo about-photo" role="img" aria-label="Builder in safety vest standing under timber roof framing"></div>
<div class="abs preheader about-pre">Hear from our founder</div>
<h2 class="abs about-title">About Founder’s</h2>
<p class="abs about-text">Lorem ipsum dolor sit amet, consectetur adipiscing elit, sed do eiusmod tempor incididunt ut labore et dolore magna aliqua. Ut enim ad minim veniam, quis nostrud exercitation ullamco laboris nisi ut aliquip ex ea commodo consequat. Duis aute irure dolor in reprehenderit. Lorem ipsum dolor sit amet, consectetur adipiscing elit.</p>
<div class="abs signature" role="img" aria-label="Handwritten signature of founder Mara L. Quenby"></div>
<span class="abs btn btn-accent about-btn">Meet The Team</span>

<h2 class="section-title" style="top:3566px">Testimonials</h2>
<div class="tcard" style="left:88px">
  <div class="avatar" role="img" aria-label="Portrait photo of client"></div>
  <div class="name">Harbor Glass Co.</div><div class="role">Project Name</div>
  <svg class="mark" width="40" height="30" viewBox="0 0 40 30" fill="#EDEDEF"><path d="M0 30V16C0 7 5 1 14 0v6c-4 1-6 4-6 8h6v16zM22 30V16c0-9 5-15 14-16v6c-4 1-6 4-6 8h6v16z"/></svg>
  <p>It is a long established fact that a reader will be distracted by the readable content of a page when looking at its layout. It is a long...</p>
</div>
<div class="tcard" style="left:528px">
  <div class="avatar" role="img" aria-label="Portrait photo of client"></div>
  <div class="name">Nadia Fenwick</div><div class="role">Project Name</div>
  <svg class="mark" width="40" height="30" viewBox="0 0 40 30" fill="#EDEDEF"><path d="M0 30V16C0 7 5 1 14 0v6c-4 1-6 4-6 8h6v16zM22 30V16c0-9 5-15 14-16v6c-4 1-6 4-6 8h6v16z"/></svg>
  <p>It is a long established fact that a reader will be distracted by the readable content of a page when looking at its layout. It is a long...</p>
</div>
<div class="tcard" style="left:976px">
  <div class="avatar" role="img" aria-label="Portrait photo of client"></div>
  <div class="name">Owen Castell</div><div class="role">Project Name</div>
  <p>It is a long established fact that a reader will be distracted by the readable content of a page when looking at its layout. It is a long...</p>
</div>

<div class="abs footer-bg"></div>
<div class="abs final-cta">
  <h2>Ready to Start?</h2>
  <p>Sometimes you need to call in the skill and trust qualified person for the perfect repair. This is where a handyman comes in handy.</p>
  <span class="btn btn-dark">Contact Us</span>
</div>

<div class="fcol" style="left:120px"><h4>Quick Links</h4><ul><li>Home</li><li>Features</li><li>Services</li><li>How It Works</li><li>About</li><li>Contact Us</li></ul></div>
<div class="fcol" style="left:336px"><h4>Information</h4><ul><li>Site Map</li><li>Terms &amp; Condition</li><li>Privacy Policy</li><li>FAQs</li><li>Customer Service</li><li>Disclaimer</li></ul></div>
<div class="fcol" style="left:532px;width:260px"><h4>Newsletter</h4><p style="line-height:1.5">Subscribe to our email address to get the latest news.</p>
  <div class="news-input"><span>Enter Your Email</span><b><svg width="14" height="14" viewBox="0 0 14 14" fill="#fff"><path d="M0 6l14-6-6 14-2-6z"/></svg></b></div></div>
<div class="fcol" style="left:864px"><h4>Contact Us</h4>
  <div class="contact-row"><svg width="14" height="14" viewBox="0 0 14 14" fill="#F5B12B"><path d="M0 2h14v10H0zM1 3l6 5 6-5"/></svg><div><strong>Email</strong>info@example.com</div></div>
  <div class="contact-row"><svg width="14" height="14" viewBox="0 0 14 14" fill="#F5B12B"><path d="M3 0l3 4-2 2c1 2 2 3 4 4l2-2 4 3-2 3C6 14 0 8 0 2z"/></svg><div><strong>Phone</strong>123-456-7890</div></div>
  <div class="contact-row"><svg width="14" height="14" viewBox="0 0 14 14" fill="#F5B12B"><path d="M7 0a5 5 0 015 5c0 4-5 9-5 9S2 9 2 5a5 5 0 015-5zm0 3a2 2 0 100 4 2 2 0 000-4z"/></svg><div><strong>Office Location</strong>Some address line goes here</div></div>
</div>
<div class="abs footer-rule"></div>
<p class="abs copyright">©Copyright 2021 | All Rights Reserved</p>
<div class="abs socials"><i></i><i></i><i></i><i></i></div>
<div class="abs to-top"><svg width="14" height="14" viewBox="0 0 14 14" fill="none" stroke="#fff" stroke-width="2"><path d="M2 9l5-5 5 5"/></svg></div>

</body>
</html>
```